Vaultrix Web Site

Hi Designers. Our web site at www.vaultrix.net.au needs a new look.

We do:

- off-site backup, every day, for vital data
- data recovery from crashed disks

We have an existing logo

Our colour is blue. Our image is about Trust and Competence

We are in Perth, Western Australia. Our photographs are local images.

We've been in business for fifteen years.

We have a second URL too: www.keep-our-records.com.au

Both URLs go to the same web site.

Would you like to take on this project?

Target Market(s)

Target market is small to medium business, with between 5 and 100 staff. Customers are mainly in Australia but can be anywhere. There are other providers who are cheaper- our point of difference is that we are highly professional and have been in the business for 15 years. personal attention is important to us- we promise Extreme Service.

Industry/Entity Type

Data Recovery

Requirements
Must have
• Our image is about Trust and Competence. Existing text from our web site can be used.
Should not have
• No moving Flash, no Flash intro

```html
<!DOCTYPE html>
<html lang="en">
<head>
<meta charset="utf-8">
<title>Vaultrix Computer Services</title>
<link rel="stylesheet" href="https://fonts.googleapis.com/css2?family=Jost:wght@400&family=Tenor+Sans&family=Open+Sans:ital,wght@1,400;1,700&family=Arimo:ital,wght@0,400;0,700;1,400&display=swap">
<style>
:root{
  --navy:#0f3a5c;
  --ink:#1d3f5e;
  --text:#2a4a6a;
  --grey-line:#d6d6d6;
  --panel-top:#e6e6e6;
  --panel-bottom:#ffffff;
  --hero-dark:#0f5a8c;
  --hero-mid:#1a78b8;
  --hero-light:#3a9ee0;
  --button-top:#8fd2f7;
  --button-bottom:#2a8fd0;
  --quote:#a8a8a8;
}
*{box-sizing:border-box;margin:0;padding:0}
html,body{width:1200px;height:845px;overflow:hidden;background:#fff}
.page{position:relative;width:1200px;height:845px;font-family:"Arimo",Arial,sans-serif;color:var(--text)}
.top-rule{position:absolute;left:0;top:0;width:1200px;height:3px;background:#dcdcdc}

.brand{position:absolute;left:138px;top:24px;height:70px;display:flex;align-items:center;gap:22px}
.brand-mark{width:64px;height:64px;border-radius:50%;background:var(--navy)}
.brand-name{font-family:"Tenor Sans",sans-serif;font-size:25px;letter-spacing:2px;color:var(--navy);border-left:1px solid #c9c9c9;padding-left:12px;line-height:66px}

.account-tab{position:absolute;left:803px;top:0;width:261px;height:43px;background:linear-gradient(#fdfdfd,#e4e4e4);border:1px solid #c8c8c8;border-top:none;border-radius:0 0 8px 8px;box-shadow:0 2px 3px rgba(0,0,0,.18);display:flex;justify-content:center;align-items:center;gap:12px;font-size:12px;color:var(--ink)}

.main-nav{position:absolute;left:146px;top:110px;width:908px;height:31px;background:linear-gradient(#ffffff,#e3e3e3);border:1px solid #cfcfcf;border-bottom:none;border-radius:16px 16px 0 0;display:flex;justify-content:space-around;align-items:center;padding:0 14px;font-family:"Tenor Sans",sans-serif;font-size:14px;letter-spacing:1.4px;color:#111}
.main-nav .sep{color:#333}

.hero{position:absolute;left:136px;top:143px;width:929px;height:307px;border-radius:4px;overflow:hidden;background:radial-gradient(ellipse at 78% 30%,var(--hero-light),var(--hero-mid) 55%,var(--hero-dark));box-shadow:0 2px 3px rgba(0,0,0,.25)}
.hero-band{position:absolute;left:0;top:153px;width:929px;height:154px;background:linear-gradient(90deg,rgba(10,50,85,.55),rgba(10,50,85,.15) 55%,rgba(255,255,255,0));}
.hero-title{position:absolute;left:34px;top:52px;font-family:"Open Sans",sans-serif;font-weight:700;font-style:italic;font-size:29px;line-height:40px;color:#fff;text-shadow:1px 2px 2px rgba(0,0,0,.35)}
.hero-lead{position:absolute;left:24px;top:170px;font-family:"Arimo",sans-serif;font-style:italic;font-size:17px;line-height:21.5px;letter-spacing:1.6px;color:#fff}
.hero-visual{position:absolute;left:352px;top:58px;width:562px;height:186px;background:linear-gradient(90deg,rgba(235,240,245,.55),rgba(255,255,255,.92));border-radius:3px}

.divider{position:absolute;left:136px;top:465px;width:929px;height:1px;background:var(--grey-line)}

.panel{position:absolute;top:475px;height:287px;background:linear-gradient(var(--panel-top),var(--panel-bottom) 70%);border:1px solid #d2d2d2;border-radius:5px;box-shadow:0 2px 3px rgba(0,0,0,.22)}
.panel-features{left:136px;width:564px}
.panel-testimonial{left:713px;width:351px}
.panel h2{position:absolute;left:11px;top:10px;font-family:"Jost",sans-serif;font-weight:400;font-size:28px;color:var(--navy)}

.feature-list{position:absolute;left:14px;top:54px;list-style:none}
.feature-list li{display:flex;align-items:center;height:23.4px;font-size:15.5px;color:var(--ink)}
.feature-list svg{width:16px;height:14px;margin-right:18px}

.quote-open,.quote-close{position:absolute;font-family:Georgia,serif;font-size:58px;color:var(--quote);line-height:1}
.quote-open{left:12px;top:40px}
.quote-close{right:16px;top:168px}
.testimonial-text{position:absolute;left:17px;top:90px;width:320px;font-size:13.5px;line-height:16.8px;color:var(--ink)}
.testimonial-author{position:absolute;left:17px;top:174px;font-size:13.5px;font-weight:700;color:#1a1a1a}

.button{position:absolute;top:254px;width:125px;height:36px;border-radius:9px;background:linear-gradient(var(--button-top),var(--button-bottom));border:1px solid #2f7fb5;box-shadow:0 1px 2px rgba(0,0,0,.3);display:flex;align-items:center;justify-content:center;font-style:italic;font-size:15px;color:#111}
.panel-features .button{left:14px}
.panel-testimonial .button{right:12px}

.footer-rule{position:absolute;left:136px;top:778px;width:929px;height:1px;background:#e3e3e3}
.site-footer{position:absolute;left:137px;top:788px;width:927px;height:50px;background:linear-gradient(#f3f3f3,#d9d9d9);border:1px solid #c9c9c9;border-radius:5px;box-shadow:0 2px 3px rgba(0,0,0,.2);display:flex;justify-content:space-between;align-items:center;padding:0 14px 0 13px;font-size:11.5px;color:#222}
.footer-nav{display:flex;gap:12px;font-size:12px;letter-spacing:1.3px}
</style>
</head>
<body>
<div class="page">
  <div class="top-rule"></div>

  <div class="brand">
    <div class="brand-mark"></div>
    <div class="brand-name">VAULTRIX</div>
  </div>

  <nav class="account-tab">
    <span>Sign up</span><span>|</span><span>Member login</span><span>|</span><span>Contact us</span>
  </nav>

  <nav class="main-nav">
    <span>HOME</span><span class="sep">|</span>
    <span>REMOTE BACKUP</span><span class="sep">|</span>
    <span>EMERGENCY DISK</span><span class="sep">|</span>
    <span>RECOVERY</span><span class="sep">|</span>
    <span>TESTIMONIALS</span><span class="sep">|</span>
    <span>ABOUT US</span>
  </nav>

  <section class="hero">
    <div class="hero-band"></div>
    <h1 class="hero-title">VAULTRIX COMPUTER<br>SERVICES</h1>
    <p class="hero-lead">We keep your business<br>records safe, always. Backup<br>your critical data off-site,<br>every night.</p>
    <div class="hero-visual" role="img" aria-label="Row of report screens showing backup charts and graphs"></div>
  </section>

  <div class="divider"></div>

  <section class="panel panel-features">
    <h2>Safe and Secure</h2>
    <ul class="feature-list">
      <li><svg viewBox="0 0 16 14"><path d="M1 8 L6 13 L15 1" fill="none" stroke="#1d3f5e" stroke-width="3"/></svg>Reliable backup is a vital part of risk management</li>
      <li><svg viewBox="0 0 16 14"><path d="M1 8 L6 13 L15 1" fill="none" stroke="#1d3f5e" stroke-width="3"/></svg>We keep your business records safe, always</li>
      <li><svg viewBox="0 0 16 14"><path d="M1 8 L6 13 L15 1" fill="none" stroke="#1d3f5e" stroke-width="3"/></svg>Database? Customer List? Financials? Contracts?</li>
      <li><svg viewBox="0 0 16 14"><path d="M1 8 L6 13 L15 1" fill="none" stroke="#1d3f5e" stroke-width="3"/></svg>Every hard disk fails one day</li>
      <li><svg viewBox="0 0 16 14"><path d="M1 8 L6 13 L15 1" fill="none" stroke="#1d3f5e" stroke-width="3"/></svg>We backup these valuable assets</li>
      <li><svg viewBox="0 0 16 14"><path d="M1 8 L6 13 L15 1" fill="none" stroke="#1d3f5e" stroke-width="3"/></svg>Critical data backup off-site, every night</li>
      <li><svg viewBox="0 0 16 14"><path d="M1 8 L6 13 L15 1" fill="none" stroke="#1d3f5e" stroke-width="3"/></svg>Located in Perth, Western Australia- the safest place on Earth</li>
    </ul>
    <div class="button">Click for More</div>
  </section>

  <section class="panel panel-testimonial">
    <h2>Testimonial</h2>
    <span class="quote-open">&ldquo;</span>
    <p class="testimonial-text">Martin you are a legend. We have an audit in progress today and I was able to illustrate a "Live" recovery. Thank you for service above and beyond the call of duty.&nbsp; We really appreciate that</p>
    <p class="testimonial-author">Owen Harlow, Keystone Advisory</p>
    <span class="quote-close">&rdquo;</span>
    <div class="button">Click for More</div>
  </section>

  <div class="footer-rule"></div>
  <footer class="site-footer">
    <span>&copy;2010 - Vaultrix Computer Services</span>
    <nav class="footer-nav">
      <span>Home</span><span>|</span><span>Remote Backup</span><span>|</span><span>Emergency Disk</span><span>|</span><span>Recovery</span><span>|</span><span>Testimonials</span><span>|</span><span>About us</span>
    </nav>
  </footer>
</div>
</body>
</html>
```